Rebrand to a Professional design

Hi, I would like to revamp this logo and coffee bag to a professional design. This will be to see to IT and other businesses for their staff.
Attached is present bag and logo. I would like a different bag type. examples attached too. the Telani girl can stay the same or you can enhance it. Its more about having a subtle seperation for acorporate brand styme.

You can’t blend in when you stand out

```html
<!DOCTYPE html>
<html lang="en">
<head>
<meta charset="utf-8">
<title>Telani Coffee – Label</title>
<link rel="stylesheet" href="https://fonts.googleapis.com/css2?family=Bevan&family=Cinzel:wght@600&family=Fraunces:opsz,wght@144,900&family=Roboto+Slab:wght@800&display=swap">
<style>
  :root {
    --roast: #4a2e25;
    --roast-deep: #3c241d;
    --cream: #f1ecea;
    --cream-muted: #d9d1cf;
    --gold-light: #f6e6c4;
    --gold: #e4c08c;
    --gold-deep: #c99f66;
    --ray: #8a6a4a;
  }
  * { margin: 0; padding: 0; box-sizing: border-box; }
  html, body { width: 1200px; height: 795px; overflow: hidden; }
  body { background: var(--roast); position: relative; }

  .label { position: absolute; inset: 0; }

  .brand-seal {
    position: absolute; left: 542px; top: 119px;
    width: 116px; height: 116px; border-radius: 50%;
    background: var(--roast-deep);
    border: 3px solid var(--gold-deep);
    display: flex; align-items: center; justify-content: center;
  }
  .brand-seal__name {
    font-family: "Roboto Slab", serif; font-weight: 800;
    font-size: 20px; color: var(--gold); letter-spacing: 0.5px;
  }

  .founded {
    position: absolute; top: 166px;
    font-family: "Roboto Slab", serif; font-weight: 800;
    font-size: 14px; color: var(--cream-muted); letter-spacing: 0.5px;
  }
  .founded--label { left: 474px; }
  .founded--year { left: 680px; }

  .family-band {
    position: absolute; left: 511px; top: 244px;
    width: 178px; height: 40px;
  }
  .family-band__text {
    position: absolute; inset: 0;
    display: flex; align-items: center; justify-content: center;
    padding-bottom: 6px;
    font-family: "Roboto Slab", serif; font-weight: 800;
    font-size: 15px; letter-spacing: 2px; color: var(--roast);
  }

  .brand-name {
    position: absolute; left: 0; right: 0; top: 292px;
    text-align: center;
    font-family: "Bevan", serif; font-size: 66px; line-height: 1;
    color: var(--cream); letter-spacing: 1px;
  }
  .brand-name sup {
    font-family: "Roboto Slab", serif; font-size: 14px;
    vertical-align: top; position: relative; top: 2px; margin-left: 2px;
  }

  .product-line {
    position: absolute; left: 0; right: 0; top: 364px;
    display: flex; align-items: center; justify-content: center; gap: 10px;
  }
  .product-line__rule { width: 50px; height: 2px; background: var(--cream-muted); }
  .product-line__text {
    font-family: "Cinzel", serif; font-weight: 600;
    font-size: 19px; letter-spacing: 10px; color: var(--cream-muted);
    padding-left: 10px;
  }

  .origin-band {
    position: absolute; left: 472px; top: 395px;
    width: 267px; height: 36px;
    background: linear-gradient(90deg, var(--gold-deep), var(--gold-light) 55%, var(--gold));
    display: flex; align-items: center; justify-content: center;
    font-family: "Fraunces", serif; font-weight: 900;
    font-size: 25px; color: var(--roast); letter-spacing: 0.3px;
  }

  .cup-illustration {
    position: absolute; left: 358px; top: 452px;
    width: 487px; height: 258px;
    background: radial-gradient(ellipse at 50% 45%, var(--cream) 0%, var(--cream-muted) 42%, var(--ray) 70%, var(--roast) 100%);
    border-radius: 8px;
  }
</style>
</head>
<body>
  <main class="label">
    <span class="founded founded--label">ESTD</span>
    <div class="brand-seal"><span class="brand-seal__name">Telani</span></div>
    <span class="founded founded--year">1984</span>

    <div class="family-band">
      <svg width="178" height="40" viewBox="0 0 178 40" aria-hidden="true">
        <path d="M2 6 L168 4 L176 2 L176 36 L2 34 Z" fill="var(--cream)"/>
      </svg>
      <span class="family-band__text">FAM.VERDO</span>
    </div>

    <h1 class="brand-name">TELANI<sup>®</sup></h1>

    <div class="product-line">
      <span class="product-line__rule"></span>
      <span class="product-line__text">COFFEE</span>
      <span class="product-line__rule"></span>
    </div>

    <div class="origin-band">100% ARABICA</div>

    <div class="cup-illustration" role="img" aria-label="Engraved illustration of a coffee cup on a saucer with two lily flowers and radiating sunburst lines"></div>
  </main>
</body>
</html>
```